Baby Care Print Log for Nannies and Parents- Creating a brand/style I can use across different forms

I am creating a notebook for babysitters to use to communicate with parents about the children they care for. I will be creating many different forms (emergency contacts, daily logs, shopping lists, etc.)
I need a look and feel from which to style these forms from. I am starting by designing the daily baby care log. I need a designer to take my Word doc with just text on it, and create a visual approach to make this visually appealing.
I do not want this to be extremely "babyish" with cartoon styling. I want it to be more of a professional looking style. I would like to be able to color each different document a different color palette, yet keep the similar look and feel. My logo is attached for inspiration. I use real photography across my website quillharborpages.com.
Updates
I will be re-designing my Wordpress website based on what design I like best and also will need other forms completed once I pick a design. I am hoping to work with someone who I can hire for further development needs as well. Added Saturday, February 11, 2017
Target Market(s)
Professional Parents
Industry/Entity Type
Education
Requirements
Must have
- color, pop, visual appeal
- Please use the color in my logo and any complementary colors that you think work well with it. I definitely like colored patterns, ombre, colored backgrounds, etc. I'd prefer for it not to be completely white with only pops of color here and there.
Nice to have
- My logo somewhere subtly on the form
- Photography elements
Should not have
- cartoon images of babies, etc. I use real photography across my website with the exception of my logo umbrella.

```html
<!DOCTYPE html>
<html lang="en">
<head>
<meta charset="utf-8">
<title>Quill Harbor Pages – Daily Baby Care Log</title>
<link href="https://fonts.googleapis.com/css2?family=Lato:wght@400;700&display=swap" rel="stylesheet">
<style>
  :root {
    --peach: #f8cbb3;
    --peach-light: #fbd8c4;
    --blush: #f3a99a;
    --blush-deep: #ee8f84;
    --panel: #fdf7f6;
    --panel-edge: #f0b3a8;
    --rule: #f1cfc8;
    --ink: #3f1a1b;
    --dot: #ee7f7c;
    --white: #ffffff;
  }
  * { box-sizing: border-box; margin: 0; padding: 0; }
  html, body { width: 927px; height: 1200px; overflow: hidden; }
  body { font-family: 'Lato', sans-serif; color: var(--ink); }
  .sheet { position: relative; width: 927px; height: 1200px; overflow: hidden; }
  .texture {
    position: absolute; inset: 0;
    background: linear-gradient(160deg, var(--peach-light) 0%, var(--peach) 55%, #f6c2a8 100%);
  }
  .swoosh { position: absolute; inset: 0; }
  .brand {
    position: absolute; left: 706px; top: 72px;
    color: var(--white); font-weight: 700; font-size: 25px; line-height: 1.05;
  }
  .label { position: absolute; font-weight: 700; font-size: 16px; white-space: nowrap; }
  .field {
    position: absolute; background: var(--panel);
    border: 1px solid var(--panel-edge); border-radius: 20px;
  }
  .panel {
    position: absolute; background: var(--panel);
    border: 1px solid var(--panel-edge); border-radius: 32px;
  }
  .rule { position: absolute; height: 1px; background: var(--rule); }
  .check {
    position: absolute; width: 27px; height: 27px; margin: -13.5px 0 0 -13.5px;
    border: 1.2px solid var(--blush-deep); border-radius: 9px; background: #fdeee8;
  }
  .col-head { position: absolute; font-weight: 700; font-size: 16px; transform: translateX(-50%); white-space: nowrap; }
  .item { position: absolute; left: 158px; font-size: 15.5px; white-space: nowrap; }
  .item::before {
    content: ""; display: inline-block; width: 6px; height: 6px; border-radius: 50%;
    background: var(--dot); margin: 0 5px 2px 2px; vertical-align: middle;
  }
</style>
</head>
<body>
<main class="sheet">
  <div class="texture" role="img" aria-label="Soft peach wood grain texture background"></div>
  <svg class="swoosh" width="927" height="1200" viewBox="0 0 927 1200" aria-hidden="true">
    <defs>
      <linearGradient id="swoosh-top" x1="0" y1="0" x2="1" y2="1">
        <stop offset="0" stop-color="#f6b7a6"/>
        <stop offset="0.55" stop-color="#fbd9cc"/>
        <stop offset="1" stop-color="#f3a394"/>
      </linearGradient>
      <linearGradient id="swoosh-bottom" x1="0" y1="0" x2="1" y2="1">
        <stop offset="0" stop-color="#f3a99a"/>
        <stop offset="1" stop-color="#f8c6b6"/>
      </linearGradient>
    </defs>
    <path d="M395 0 C520 90 640 170 760 230 C830 265 880 290 927 322 L927 0 Z" fill="url(#swoosh-top)"/>
    <path d="M0 1040 C60 1080 120 1140 170 1200 L0 1200 Z" fill="url(#swoosh-bottom)"/>
  </svg>

  <div class="brand">Quill<br>Harbor<br>Pages</div>

  <div class="label" style="left:152px; top:168px;">NameDate</div>
  <div class="field" style="left:150px; top:190px; width:357px; height:39px;"></div>

  <div class="label" style="left:152px; top:241px;">Nan TimeFeeding</div>
  <div class="field" style="left:150px; top:265px; width:123px; height:39px;"></div>

  <section class="panel" style="left:147px; top:315px; width:638px; height:237px;"></section>
  <div class="label" style="left:190px; top:340px;">TimeHow LongTimeMilk(Type)</div>
  <div class="col-head" style="left:493px; top:340px;">Water</div>
  <div class="col-head" style="left:586px; top:340px;">Food</div>
  <div class="col-head" style="left:683px; top:340px;">Amount</div>
  <div class="rule" style="left:184px; top:404px; width:245px;"></div>
  <div class="rule" style="left:184px; top:438px; width:245px;"></div>
  <div class="rule" style="left:184px; top:473px; width:245px;"></div>
  <div class="rule" style="left:184px; top:507px; width:245px;"></div>
  <div class="rule" style="left:460px; top:404px; width:67px;"></div>
  <div class="rule" style="left:460px; top:438px; width:67px;"></div>
  <div class="rule" style="left:460px; top:473px; width:67px;"></div>
  <div class="rule" style="left:460px; top:507px; width:67px;"></div>
  <div class="rule" style="left:553px; top:404px; width:67px;"></div>
  <div class="rule" style="left:553px; top:438px; width:67px;"></div>
  <div class="rule" style="left:553px; top:473px; width:67px;"></div>
  <div class="rule" style="left:553px; top:507px; width:67px;"></div>
  <div class="rule" style="left:650px; top:404px; width:67px;"></div>
  <div class="rule" style="left:650px; top:438px; width:67px;"></div>
  <div class="rule" style="left:650px; top:473px; width:67px;"></div>
  <div class="rule" style="left:650px; top:507px; width:67px;"></div>

  <section class="panel" style="left:143px; top:559px; width:645px; height:308px;"></section>
  <div class="label" style="left:165px; top:583px;">DiapersMood</div>
  <div class="label" style="left:165px; top:615px;">TimeWetBMHappy</div>
  <div class="col-head" style="left:350px; top:615px;">Sad</div>
  <div class="col-head" style="left:424px; top:615px;">Unsettled</div>
  <div class="col-head" style="left:506px; top:615px;">Energetic</div>
  <div class="col-head" style="left:582px; top:615px;">Tired</div>
  <div class="col-head" style="left:661px; top:615px;">Chatty</div>
  <div class="col-head" style="left:734px; top:615px;">Quiet</div>

  <div class="rule" style="left:166px; top:665px; width:143px;"></div>
  <div class="rule" style="left:166px; top:699px; width:143px;"></div>
  <div class="rule" style="left:166px; top:733px; width:143px;"></div>
  <div class="rule" style="left:166px; top:766px; width:143px;"></div>
  <div class="rule" style="left:166px; top:800px; width:143px;"></div>
  <div class="rule" style="left:166px; top:834px; width:143px;"></div>

  <div class="check" style="left:350px; top:653px;"></div><div class="check" style="left:424px; top:653px;"></div><div class="check" style="left:506px; top:653px;"></div><div class="check" style="left:582px; top:653px;"></div><div class="check" style="left:659px; top:653px;"></div><div class="check" style="left:736px; top:653px;"></div>
  <div class="check" style="left:350px; top:686px;"></div><div class="check" style="left:424px; top:686px;"></div><div class="check" style="left:506px; top:686px;"></div><div class="check" style="left:582px; top:686px;"></div><div class="check" style="left:659px; top:686px;"></div><div class="check" style="left:736px; top:686px;"></div>
  <div class="check" style="left:350px; top:720px;"></div><div class="check" style="left:424px; top:720px;"></div><div class="check" style="left:506px; top:720px;"></div><div class="check" style="left:582px; top:720px;"></div><div class="check" style="left:659px; top:720px;"></div><div class="check" style="left:736px; top:720px;"></div>
  <div class="check" style="left:350px; top:754px;"></div><div class="check" style="left:424px; top:754px;"></div><div class="check" style="left:506px; top:754px;"></div><div class="check" style="left:582px; top:754px;"></div><div class="check" style="left:659px; top:754px;"></div><div class="check" style="left:736px; top:754px;"></div>
  <div class="check" style="left:350px; top:788px;"></div><div class="check" style="left:424px; top:788px;"></div><div class="check" style="left:506px; top:788px;"></div><div class="check" style="left:582px; top:788px;"></div><div class="check" style="left:659px; top:788px;"></div><div class="check" style="left:736px; top:788px;"></div>
  <div class="check" style="left:350px; top:822px;"></div><div class="check" style="left:424px; top:822px;"></div><div class="check" style="left:506px; top:822px;"></div><div class="check" style="left:582px; top:822px;"></div><div class="check" style="left:659px; top:822px;"></div><div class="check" style="left:736px; top:822px;"></div>

  <div class="label" style="left:158px; top:887px;">Today Activities</div>
  <div class="field" style="left:300px; top:879px; width:476px; height:37px;"></div>

  <div class="label" style="left:158px; top:928px;">Supplies Needed Soon</div>
  <div class="item" style="top:957px;">DiapersMilk/FormulaWet Wipes</div>
  <div class="item" style="top:991px;">Diaper CreamCerealBaby Food</div>
  <div class="item" style="top:1025px;">Other:</div>
  <div class="field" style="left:227px; top:1015px; width:549px; height:38px;"></div>

  <div class="label" style="left:165px; top:1058px;">Special Notes</div>
  <div class="rule" style="left:166px; top:1098px; width:600px;"></div>
  <div class="rule" style="left:166px; top:1118px; width:600px;"></div>
  <div class="rule" style="left:166px; top:1138px; width:600px;"></div>
</main>
</body>
</html>
```